Heath Weight Loss Retreat Website

The brief:
PineLoop is a provider of health & weight loss retreats and wish to redesign their main website. The website needs to provide detailed information about the company’s services whilst gathering the maximum number of leads possible. The website does not aim to get clients to ‘book now’ but to request further information, or ask a question generating a lead/opportunity for the business.

Primary objectives of website
• Gather leads for products (not necessarily to book at that point, but to ‘request more info’)
• Provide detailed information about the health and fitness programs on offer

Demographic Considerations
• Target age group: 30-50
• Predominant client base are female but website should be gender neutral due to some men attending

Design considerations
• Essentially selling ‘travel experiences’ and ‘life transformations’ so needs to be lots of images to display (similar to a hotel website for example)
• Images need to display real people – i.e. larger people, rather than super thin
• Not too much use of flash
• SEO friendly (we have good rankings at present)
• Will be implemented into Joomla, so please consider this on the design
• Colours should be ‘warm’ and ‘friendly’ and gender neutral

Project Requirements & Expectations
Please supply your design ideas with:
• At least 1 (preferably more) homepage examples
• At least 1 (preferably more) internal page examples
Once a preferred design has been selected the following will be produced, tweaked and approved:
• Homepage + 1 internal landing page + 1 internal main page + 1 contact page + 1 info request page

Attachments
We have attached both a homepage and internal page example which demonstates the type of content needed and the calls to action. This is for demonstration purposes only so please ignore colours, fonts, etc and provide your best designs based on a general layout as per attached.

Images:
A selection of example images has been attached. For the homepage images of the retreats themselves should be used alongside images of ‘larger people’.

Further information:
Please contact Simon Thackery at simon.thackery@coralbeaconfiles.com.au

Target Market(s)

Overweight females aged 30-50 are the main target market. However must be gender neutral due to some men using product.

Industry/Entity Type

Weight

Requirements
Should not have
• Not too much flash

```html
<!DOCTYPE html>
<html lang="en">
<head>
<meta charset="utf-8">
<title>PineLoop Weight Loss Retreat</title>
<link rel="stylesheet" href="https://fonts.googleapis.com/css2?family=Arimo:ital,wght@0,400;0,700;1,400;1,700&display=swap">
<style>
:root{
  --green:#2f8a1f;
  --green-dark:#256e17;
  --green-soft:#e6f7dc;
  --green-line:#3c9a2a;
  --orange:#f08400;
  --orange-soft:#fde3b8;
  --text:#111;
  --panel-border:#d9ead3;
  --grey:#e9e9e9;
}
*{box-sizing:border-box;margin:0;padding:0}
html,body{width:893px;height:1200px;overflow:hidden;background:#fff}
body{font-family:"Arimo",Arial,sans-serif;color:var(--text)}
.page{position:relative;width:960px;height:1290px;transform:scale(.9302);transform-origin:0 0}
.abs{position:absolute}
a{color:var(--orange);text-decoration:underline}
.panel{position:absolute;background:#fff;border:1px solid var(--panel-border);border-radius:12px;box-shadow:0 2px 4px rgba(0,0,0,.15)}
.brand{left:28px;top:22px;display:flex;align-items:center;gap:8px}
.brand-dot{width:26px;height:26px;border-radius:50%;background:var(--orange)}
.brand-name{font-size:28px;font-weight:700;color:var(--green);letter-spacing:.5px}
.banner{left:241px;top:10px;width:480px;height:60px;background:linear-gradient(#f4f4f4,#e2e2e2);border:1px solid #ccc;box-shadow:0 2px 3px rgba(0,0,0,.2);display:flex;align-items:center;justify-content:center;font-size:24px;font-weight:700;color:#fff;text-shadow:0 0 2px #999}
.social{top:20px;width:32px;height:32px;border-radius:5px;background:#8fbf7f}
.nav-line{left:0;width:960px;height:3px;background:var(--green)}
.nav{left:0;top:85px;width:960px;height:22px;background:linear-gradient(#f6fdf2,#dff3d6);font-size:12px}
.nav span{position:absolute;top:4px}
.caret{font-size:9px;color:#333}
.hero-img{left:22px;top:130px;width:698px;height:260px;border-radius:3px;background:linear-gradient(160deg,#2f3b22 0%,#6d7e5a 30%,#d7ddd0 45%,#4f7a2c 65%,#2f4a18 100%)}
.hero-cap{left:35px;top:318px;width:673px;height:62px;background:rgba(220,240,205,.85);border:1px solid #6fa34f;font-size:11px}
.dots{left:598px;top:320px;display:flex;gap:3px}
.dots i{width:12px;height:12px;border-radius:50%;background:#fff6c0;border:1px solid var(--orange);display:block}
.dots i:first-child{background:var(--green)}
.photo{background:linear-gradient(160deg,#7c8f6a,#c9b79c 60%,#50603e)}
h2.section{font-size:18px;color:var(--green);font-weight:700}
.btn{top:656px;height:24px;border:1px solid var(--orange);border-radius:4px;background:linear-gradient(#fde3b0,#f9b04a);font-size:14px;font-weight:700;display:flex;align-items:center;justify-content:center}
.features{font-size:12px;font-weight:700;line-height:15px}
.rule{left:25px;width:695px;height:2px;background:#999}
.body-copy{left:36px;width:686px;font-size:12px;line-height:14.6px;letter-spacing:-.15px}
.body-copy p+p{margin-top:14px}
.body-copy a{font-style:italic}
.side-h{font-size:18px;color:var(--green);font-weight:700}
.loc{left:743px;width:202px;border-radius:2px;color:#fff;font-size:9px;padding:6px 10px}
.loc b{font-size:12px;display:block}
.loc a{color:#fff;font-weight:700}
.prog{left:753px;font-size:12px;line-height:14.5px}
.prog b{color:var(--green)}
.footer{font-size:11px}
.footer a{color:#333}
</style>
</head>
<body>
<div class="page">

  <header>
    <div class="abs brand"><span class="brand-dot"></span><span class="brand-name">PineLoop</span></div>
    <div class="abs banner">Posible Banner</div>
    <span class="abs social" style="left:760px"></span>
    <span class="abs social" style="left:806px"></span>
    <span class="abs social" style="left:852px"></span>
    <span class="abs social" style="left:898px"></span>
  </header>

  <div class="abs nav-line" style="top:81px"></div>
  <nav class="abs nav">
    <span style="left:34px">Home</span>
    <span style="left:136px">About Us</span><span class="caret" style="left:218px">▽</span>
    <span style="left:254px;text-decoration:underline">The Best Programs</span><span class="caret" style="left:393px">▽</span>
    <span style="left:429px">To Know More</span><span class="caret" style="left:539px">▽</span>
    <span style="left:575px">Free Information</span><span class="caret" style="left:697px">▽</span>
    <span style="left:733px">Contact Us</span>
    <span style="left:862px">Book Now</span>
  </nav>
  <div class="abs nav-line" style="top:107px"></div>

  <!-- Hero -->
  <section class="panel" style="left:10px;top:120px;width:720px;height:280px"></section>
  <div class="abs hero-img" role="img" aria-label="Waterfall over mossy rocks at a retreat location"></div>
  <div class="abs hero-cap">
    <div style="position:absolute;left:7px;top:3px;font-size:14px;font-weight:700;color:var(--green)">Amazing weight loss &amp; fitness results</div>
    <div style="position:absolute;left:21px;top:19px;font-style:italic;font-size:12px">Lasting results &amp; 1st class facilities</div>
    <div style="position:absolute;left:32px;top:33px">PineLoop has helped hundreds of people transform their lives, lose weight, get fit and achieve lasting success.</div>
    <div style="position:absolute;left:20px;top:46px">Let us help you too... <a style="font-style:italic">Read More&gt;&gt;</a></div>
  </div>
  <div class="abs dots"><i></i><i></i><i></i><i></i><i></i><i></i><i></i></div>

  <!-- Real people -->
  <section class="panel" style="left:10px;top:410px;width:720px;height:160px"></section>
  <div class="abs photo" style="left:22px;top:425px;width:80px;height:60px" role="img" aria-label="Client reading a book"></div>
  <div class="abs photo" style="left:113px;top:425px;width:70px;height:60px" role="img" aria-label="Smiling client portrait"></div>
  <div class="abs photo" style="left:22px;top:490px;width:75px;height:64px" role="img" aria-label="Client outdoors by a tree"></div>
  <div class="abs photo" style="left:113px;top:490px;width:70px;height:64px" role="img" aria-label="Client portrait"></div>
  <div class="abs photo" style="left:557px;top:425px;width:80px;height:60px" role="img" aria-label="Client reading a book"></div>
  <div class="abs photo" style="left:648px;top:425px;width:70px;height:60px" role="img" aria-label="Smiling client portrait"></div>
  <div class="abs photo" style="left:557px;top:490px;width:75px;height:64px" role="img" aria-label="Client outdoors by a tree"></div>
  <div class="abs photo" style="left:648px;top:490px;width:70px;height:64px" role="img" aria-label="Client portrait"></div>
  <div class="abs" style="left:248px;top:419px;font-size:16px;font-weight:700;color:var(--green)">Real People - Real Results</div>
  <div class="abs" style="left:285px;top:442px;font-size:12px;line-height:14.5px">- 100's of people helped by PineLoop<br>- People of all ages, shapes, and sizes<br>- Normal people just like you</div>
  <a class="abs" style="left:248px;top:500px;font-size:12px;font-style:italic">Testimonials and reviews&gt;&gt;</a>

  <!-- Quote & CTA -->
  <section class="panel" style="left:10px;top:580px;width:498px;height:160px"></section>
  <div class="abs" style="left:17px;top:587px;width:483px;height:148px;background:var(--green-soft);border:1px solid var(--orange)"></div>
  <div class="abs" style="left:21px;top:593px;font-size:13px;font-weight:700;font-style:italic">The PineLoop program works - as one client put it...</div>
  <div class="abs" style="left:21px;top:614px;font-size:22px;font-weight:700;font-style:italic;color:var(--green)">“The Best Weight loss Experience of my life”</div>
  <div class="abs btn" style="left:23px;width:287px">Request a FREE information pack &gt;&gt;</div>
  <div class="abs btn" style="left:319px;width:171px">More Testimonials</div>
  <div class="abs features" style="left:56px;top:698px">- Stunning Locations<br>- 1st class facilities</div>
  <div class="abs features" style="left:200px;top:698px">- Amazing results<br>- For al shapes &amp; sizes</div>
  <div class="abs features" style="left:344px;top:698px">- Delicious healty food<br>- Expert Support</div>

  <!-- Testimonial -->
  <section class="panel" style="left:520px;top:580px;width:210px;height:160px"></section>
  <svg class="abs" style="left:538px;top:588px" width="180" height="146" viewBox="0 0 180 146">
    <defs><linearGradient id="tri" x1="0" y1="0" x2="0" y2="1"><stop offset="0" stop-color="#5fb146"/><stop offset="1" stop-color="#2f8a1f"/></linearGradient></defs>
    <polygon points="90,0 180,15 0,15" fill="url(#tri)"/>
    <polygon points="0,128 180,128 90,142" fill="url(#tri)"/>
  </svg>
  <div class="abs" style="left:527px;top:612px;width:195px;height:96px;background:var(--green-soft);border:1px solid var(--orange)"></div>
  <div class="abs" style="left:536px;top:628px;font-size:17px;font-style:italic;color:var(--green);line-height:22px">“The best weight loss<br>&nbsp;experience in my life”</div>
  <div class="abs" style="left:536px;top:670px;font-size:11px;font-style:italic;color:var(--orange)">(Name of the person)</div>

  <!-- Transform -->
  <section class="panel" style="left:10px;top:750px;width:720px;height:482px"></section>
  <h2 class="abs section" style="left:27px;top:761px">PineLoop Transforms Your Life</h2>
  <div class="abs rule" style="top:790px"></div>
  <div class="abs rule" style="top:898px"></div>
  <div class="abs rule" style="top:1006px"></div>
  <div class="abs rule" style="top:1114px"></div>
  <div class="abs rule" style="top:1214px"></div>
  <div class="abs body-copy" style="top:798px"><p>Hundreds of people hhave already transformed their lives with PineLoop's proven programs. With PineLoop you will lose weight, lose centimetres, get fit and experience lasting health and fitness results.</p><p>Our <a>Weight Loss Retreat </a>program is suitable for people of all ages, shapes, sizes and fitness levels. It is amazingly fun and extremely effective with amazing weight loss and fitness results. Whether you want a kick start or are embarking on a long term weight loss program our <a>Weight Loss Retreat</a> program will be one of the best experiences of your life - that's our promise to you.</p></div>
  <div class="abs body-copy" style="top:906px"><p>Hundreds of people hhave already transformed their lives with PineLoop's proven programs. With PineLoop you will lose weight, lose centimetres, get fit and experience lasting health and fitness results.</p><p>Our <a>Weight Loss Retreat </a>program is suitable for people of all ages, shapes, sizes and fitness levels. It is amazingly fun and extremely effective with amazing weight loss and fitness results. Whether you want a kick start or are embarking on a long term weight loss program our <a>Weight Loss Retreat</a> program will be one of the best experiences of your life - that's our promise to you.</p></div>
  <div class="abs body-copy" style="top:1014px"><p>Hundreds of people hhave already transformed their lives with PineLoop's proven programs. With PineLoop you will lose weight, lose centimetres, get fit and experience lasting health and fitness results.</p><p>Our <a>Weight Loss Retreat </a>program is suitable for people of all ages, shapes, sizes and fitness levels. It is amazingly fun and extremely effective with amazing weight loss and fitness results. Whether you want a kick start or are embarking on a long term weight loss program our <a>Weight Loss Retreat</a> program will be one of the best experiences of your life - that's our promise to you.</p></div>
  <div class="abs body-copy" style="top:1122px"><p>Hundreds of people hhave already transformed their lives with PineLoop's proven programs. With PineLoop you will lose weight, lose centimetres, get fit and experience lasting health and fitness results.</p><p>Our <a>Weight Loss Retreat </a>program is suitable for people of all ages, shapes, sizes and fitness levels. It is amazingly fun and extremely effective with amazing weight loss and fitness results. Whether you want a kick start or are embarking on a long term weight loss program our <a>Weight Loss Retreat</a> program will be one of the best experiences of your life - that's our promise to you.</p></div>

  <!-- Sidebar: magazine -->
  <section class="panel" style="left:740px;top:120px;width:210px;height:120px"></section>
  <div class="abs" style="left:754px;top:128px;width:72px;height:98px;background:linear-gradient(150deg,#1d2a6b,#e8e8f0 40%,#d84a4a 75%,#3b6cc0)" role="img" aria-label="Fanned magazine covers"></div>
  <div class="abs" style="left:836px;top:152px;font-size:18px;font-weight:700;font-style:italic;color:var(--green)">FREE</div>
  <div class="abs" style="left:836px;top:171px;font-size:11.5px;font-weight:700;color:var(--green)">PineLoop Magazine</div>
  <a class="abs" style="left:836px;top:186px;font-size:12px;font-style:italic">Request Now &gt;&gt;</a>

  <!-- Goal selector -->
  <section class="panel" style="left:740px;top:250px;width:210px;height:112px"></section>
  <div class="abs" style="left:747px;top:257px;width:196px;height:97px;background:var(--orange-soft);border:1px solid var(--orange)"></div>
  <div class="abs" style="left:754px;top:266px;font-size:18px;font-weight:700;color:var(--green)">Your Goal Selector</div>
  <div class="abs" style="left:754px;top:286px;font-size:12px;font-style:italic;line-height:15px">Tell us your goal and we'll tell you<br>how PineLoop can help:</div>
  <div class="abs" style="left:754px;top:320px;width:147px;height:22px;background:#fff;border:1px solid #999"></div>
  <div class="abs" style="left:907px;top:320px;width:28px;height:22px;background:#fff;border:1px solid #999;font-size:12px;font-style:italic;display:flex;align-items:center;justify-content:center">Go</div>

  <!-- Locations -->
  <section class="panel" style="left:740px;top:375px;width:210px;height:290px"></section>
  <div class="abs side-h" style="left:750px;top:386px">The Best Locations</div>
  <div class="abs" style="left:748px;top:408px;font-size:14px;font-style:italic">&amp; 1<sup style="font-size:8px">st</sup> class facilities</div>
  <div class="abs loc" style="top:437px;height:76px;background:linear-gradient(#f6fbff,#b7cfa7 60%,#4d7a3b);color:#222" role="img" aria-label="Blue Mountains retreat scenery">
    <b style="color:#222;margin-top:2px">Blue Mountains ****</b>
    <span style="font-style:italic">4 star accommodation, stunning mountain scenery &amp; 1st class facilities</span><br>
    <a style="color:#1a3d8f">Find out more</a> | <a style="color:#1a3d8f">FREE Brochure</a> | <a style="color:#1a3d8f">Book</a>
  </div>
  <div class="abs loc" style="top:519px;height:63px;background:linear-gradient(#4e79b7,#cfe1f1 45%,#4f8a58)" role="img" aria-label="Sunshine Coast beach resort">
    <b>Sunshine Coast ****</b><span style="font-style:italic">4.5 star accommodation</span><br><a>Find out more</a> | <a>FREE Brochure</a> | <a>Book</a>
  </div>
  <div class="abs loc" style="top:590px;height:63px;background:linear-gradient(#4e79b7,#cfe1f1 45%,#4f8a58)" role="img" aria-label="Sunshine Coast beach resort">
    <b>Sunshine Coast ****</b><span style="font-style:italic">4.5 star accommodation</span><br><a>Find out more</a> | <a>FREE Brochure</a> | <a>Book</a>
  </div>

  <!-- Programs -->
  <section class="panel" style="left:740px;top:675px;width:210px;height:557px"></section>
  <div class="abs side-h" style="left:753px;top:689px">The Best Programs</div>
  <a class="abs" style="left:753px;top:708px;font-size:12px;font-style:italic">Book Now&gt;&gt;</a>
  <div class="abs prog" style="top:750px"><b>Weight Loss Retreat</b><br><i>Lasting weight loss results</i><br><a>Program details</a> | <a>Typical Day</a><br><a>Dates &amp; Rates</a> | <a>FREE Brochure</a></div>
  <div class="abs prog" style="top:836px"><b>Residential Boot Camp</b><br><i>Kick start your health &amp; fitness</i><br><a>Program details</a> | <a>Typical Day</a><br><a>Dates &amp; Rates</a> | <a>FREE Brochure</a></div>
  <div class="abs prog" style="top:923px"><b>At Home Program</b><br><i>Do it yourself with our home pack</i><br><a>Program details</a> | <a>FREE Brochure</a></div>
  <div class="abs prog" style="top:995px"><b>Fitness Days</b><br><i>Have fun and keep on track</i><br><a>Program overview</a> | <a>Typical Day</a><br><a>Dates &amp; Rates</a> | <a>FREE Brochure</a></div>
  <div class="abs prog" style="top:1081px"><b>Local Group Exercise</b><br><i>Get fit &amp; lose weight locally</i><br><a>Overview</a> | <a>Tipes &amp; Locations</a></div>
  <div class="abs prog" style="top:1153px"><b>Personal Training for you</b><br><a>Find an approved PineLoop Trainer</a></div>

  <!-- Footer -->
  <div class="abs nav-line" style="top:1250px"></div>
  <div class="abs footer" style="left:25px;top:1260px">Copyright PineLoop Wellbeing PTY Ltd &nbsp;|&nbsp; ABN 1234567987</div>
  <div class="abs footer" style="left:723px;top:1258px"><a>Contact Us</a> &nbsp;|&nbsp; <a>Book Now</a> &nbsp;|&nbsp; <a>FAQ</a> &nbsp;|&nbsp; <a>Privacy</a></div>
  <div class="abs nav-line" style="top:1277px"></div>

</div>
</body>
</html>
```